New Card

Photography business
I want a sleek simple card that screams rich and classy. Black/Gold or silver font. No photos or images but would love a new logo When I hand someone my card I want compliments
Updates
My fiancé reminded me in 5 short months my name will change so I have changed my name to Colleen Abernathy
Also my BRAND is Lantern Field Photography, not my name. Thanks
Industry/Entity Type
Business
Contact Information for Business Card
Lantern Field Photography
Colleen Abernathy-owner
274 W. Hollis Ave.
Millbrook Point, NJ 08099
(856)555-0143
colleen@lanternfieldphotos.example
Look and feel
Each slider illustrates characteristics of the customer's brand and the style your logo design should communicate.

```html
<!DOCTYPE html>
<html lang="en">
<head>
<meta charset="utf-8">
<title>Lantern Field Photography — Business Card</title>
<link rel="stylesheet" href="https://fonts.googleapis.com/css2?family=Federo&family=Mulish:wght@400&display=swap">
<style>
  :root {
    --page: #f4f4f4;
    --card-deep: #0b0b0b;
    --card-mid: #1e1e1e;
    --gold: #c9a43a;
    --gold-light: #ecd17a;
    --gold-dark: #8a6a1c;
    --silver: #d8d8d8;
    --silver-soft: #b9b9b9;
  }
  * { box-sizing: border-box; margin: 0; padding: 0; }
  html, body { width: 1200px; height: 900px; overflow: hidden; }
  body {
    background: var(--page);
    position: relative;
  }
  .card {
    position: absolute;
    top: 305px;
    width: 500px;
    height: 290px;
    border-radius: 22px;
    background: radial-gradient(ellipse at 50% 42%, var(--card-mid) 0%, var(--card-deep) 75%);
    box-shadow: 0 14px 28px rgba(0,0,0,0.22);
    overflow: hidden;
  }
  .card--front { left: 70px; }
  .card--back { left: 630px; }

  .gold-frame {
    position: absolute;
    inset: 11px;
    border-radius: 16px;
    border: 4px solid var(--gold);
    box-shadow: inset 0 0 0 1px var(--gold-dark), 0 0 0 1px var(--gold-dark);
  }
  .brand {
    position: absolute;
    left: 0; right: 0;
    top: 78px;
    display: flex;
    flex-direction: column;
    align-items: center;
  }
  .brand__mark {
    width: 78px;
    height: 78px;
    border-radius: 50%;
    background: radial-gradient(circle at 40% 35%, var(--gold-light), var(--gold) 55%, var(--gold-dark));
    margin-bottom: 10px;
  }
  .brand__name {
    font-family: "Federo", sans-serif;
    font-size: 29px;
    color: var(--gold);
    text-align: center;
    line-height: 1.1;
    letter-spacing: 0.5px;
  }

  .back-accent {
    position: absolute;
    right: -70px;
    top: 20px;
    width: 250px;
    height: 250px;
    border-radius: 50%;
    background: rgba(255,255,255,0.035);
  }
  .contact {
    position: absolute;
    left: 0; right: 0;
    top: 72px;
    padding-left: 90px;
    text-align: center;
  }
  .contact__name {
    font-family: "Federo", sans-serif;
    font-size: 22px;
    color: var(--gold);
  }
  .contact__role {
    font-family: "Mulish", sans-serif;
    font-size: 13px;
    color: var(--silver-soft);
    margin-top: 2px;
  }
  .contact__phone {
    font-family: "Mulish", sans-serif;
    font-size: 21px;
    color: var(--silver);
    margin-top: 38px;
  }
  .contact__line {
    font-family: "Mulish", sans-serif;
    font-size: 15px;
    color: var(--silver);
    margin-top: 2px;
    white-space: nowrap;
  }
</style>
</head>
<body>
  <section class="card card--front" aria-label="Card front">
    <div class="gold-frame"></div>
    <div class="brand">
      <div class="brand__mark"></div>
      <p class="brand__name">Lantern Field<br>Photography</p>
    </div>
  </section>

  <section class="card card--back" aria-label="Card back">
    <div class="back-accent"></div>
    <div class="contact">
      <p class="contact__name">Colleen Abernathy</p>
      <p class="contact__role">Owner</p>
      <p class="contact__phone">(856)555-0143</p>
      <p class="contact__line">colleen@lanternfieldphotos.example</p>
      <p class="contact__line">274 W. Hollis Ave. Millbrook Point, NJ 08099</p>
    </div>
  </section>
</body>
</html>
```